Skincare Cleanser Bottle Label

New product launch of a mint facial cleanser.
Brand is called Dorvelle.
Product will be called Lunara.
Looking for a label design that can be printed using silk screening.
High gloss white plastic bottle. 8oz. White push pump top.
Clinical skincare brand, professional image, sold in medical spas.

Target Market(s)

Women Age 20-65

Industry/Entity Type

Health And Wellness

Font styles to use
Serif
Sans Serif

Requirements
Must have
• Dorvelle brand name in the orignal font.
Should not have
• Multiple colours.

```html
<!DOCTYPE html>
<html lang="en">
<head>
<meta charset="utf-8">
<title>Dorvelle Lunara – Mint Facial Cleanser Label</title>
<link href="https://fonts.googleapis.com/css2?family=Josefin+Slab:wght@400;600&family=Fira+Sans:ital,wght@0,300;0,400;1,300;1,400&display=swap" rel="stylesheet">
<style>
  :root {
    --page-bg: #f4f4f4;
    --label-white: #ffffff;
    --ink: #2b2b2b;
    --teal: #1495b0;
    --teal-deep: #0a7f9a;
    --rule: #8a8a8a;
    --mint-light: #5dbb4a;
    --mint-dark: #1f7a25;
  }
  html, body {
    margin: 0;
    padding: 0;
    width: 900px;
    height: 1200px;
    overflow: hidden;
    background: var(--page-bg);
  }
  .canvas {
    position: relative;
    width: 900px;
    height: 1200px;
  }
  .label {
    position: absolute;
    left: 310px;
    top: 260px;
    width: 280px;
    height: 820px;
    background: var(--label-white);
    border-radius: 18px;
    box-shadow: 0 1px 3px rgba(0,0,0,0.06);
  }
  .brand-name {
    position: absolute;
    left: 0;
    top: 305px;
    width: 900px;
    text-align: center;
    margin: 0;
    font-family: "Josefin Slab", serif;
    font-weight: 600;
    font-size: 34px;
    letter-spacing: 0.5px;
    color: var(--ink);
  }
  .product-band {
    position: absolute;
    left: 377px;
    top: 430px;
    width: 150px;
    height: 365px;
  }
  .product-name {
    font-family: "Fira Sans", sans-serif;
    font-style: italic;
    font-weight: 300;
    font-size: 100px;
    fill: var(--label-white);
  }
  .product-type {
    font-family: "Fira Sans", sans-serif;
    font-style: italic;
    font-weight: 300;
    font-size: 19px;
    fill: var(--label-white);
  }
  .mint-visual {
    position: absolute;
    left: 355px;
    top: 765px;
    width: 195px;
    height: 155px;
    border-radius: 50%;
    background: radial-gradient(circle at 50% 45%, var(--mint-light), var(--mint-dark) 75%, rgba(31,122,37,0) 100%);
  }
  .product-details {
    position: absolute;
    left: 0;
    top: 970px;
    width: 900px;
    text-align: center;
    font-family: "Fira Sans", sans-serif;
    color: var(--ink);
  }
  .product-tagline {
    display: inline-block;
    margin: 0;
    padding: 2px 2px 3px;
    border-top: 1px solid var(--rule);
    border-bottom: 1px solid var(--rule);
    font-size: 22px;
    font-weight: 300;
    line-height: 30px;
  }
  .product-volume {
    margin: 10px 0 0;
    font-size: 17px;
    font-weight: 400;
  }
  .product-volume em { font-style: italic; }
</style>
</head>
<body>
<div class="canvas">
  <div class="label"></div>

  <h1 class="brand-name">dorvelle</h1>

  <svg class="product-band" viewBox="0 0 150 365" xmlns="http://www.w3.org/2000/svg">
    <defs>
      <linearGradient id="bandFill" x1="0" y1="0" x2="1" y2="0">
        <stop offset="0" stop-color="var(--teal)"/>
        <stop offset="1" stop-color="var(--teal-deep)"/>
      </linearGradient>
    </defs>
    <path d="M0 0 H115 A35 35 0 0 1 150 35 V365 H60 A60 60 0 0 1 0 305 Z" fill="url(#bandFill)"/>
    <text class="product-name" transform="translate(93 332) rotate(-90)">lunara</text>
    <text class="product-type" transform="translate(119 236) rotate(-90)">mint facial cleanser</text>
  </svg>

  <div class="mint-visual" role="img" aria-label="Sprig of fresh green mint leaves"></div>

  <div class="product-details">
    <p class="product-tagline">lorem ipsum</p>
    <p class="product-volume">250 <em>ml</em></p>
  </div>
</div>
</body>
</html>
```